Quiver Upcoming Gigs

One page graphic with my upcoming dates. Logo and photo attached, and sample from last flyer. Text:

QUIVER

UPCOMING DATES

3/26/18 Velvet Grotto (Las Vegas, NV)

4/1/18 Lantern Hall 2847 M St (Sac, CA)

4/8/18 Blue Heron (Sac, CA)

5/5/18 Open Lanes @ Silver Otter (Sac, CA)

5/10/18 Dunmore Fine Gallery (Sac, CA)

5/11/18 Bas Rive @ Cafe du Pont (Sac, CA)

5/27/18 Sunloft LBW @ Vox (Sac, CA)

Save The Date: 9/21/18 Moonweaver Festival (Puerto Nuevo, MX)

nightlist.net/quiver530

Target Market(s)

House/Electronic Music

Industry/Entity Type

Night Club

Font styles to use
Sans Serif

Colors

Designer to choose colors to be used in the design.

Requirements
Must have
• Quiver logo or something that looks good instead. Prefer photo to be in but not necessary.
Nice to have

```html
<!DOCTYPE html>
<html lang="en">
<head>
<meta charset="utf-8">
<title>Quiver – Upcoming Dates</title>
<link href="https://fonts.googleapis.com/css2?family=Roboto:wght@300;400&family=Roboto+Condensed:wght@400;700;800&display=swap" rel="stylesheet">
<style>
  :root {
    --page-bg: #e9e9ec;
    --card-dark: #050410;
    --card-purple: #3a1fb0;
    --card-violet: #6a2fd0;
    --logo-pink: #f2304f;
    --heading-orange: #e0553a;
    --date-white: #f2f2f2;
    --venue-yellow: #ffe23c;
    --city-white: #e6e6e6;
    --save-orange: #ffa24a;
    --link-blue: #6d5cff;
  }
  * { margin: 0; padding: 0; box-sizing: border-box; }
  html, body { width: 1200px; height: 1200px; overflow: hidden; background: var(--page-bg); }
  .stage { position: relative; width: 1200px; height: 1200px; }
  .card {
    position: absolute; left: 30px; top: 303px;
    width: 1204px; height: 627px;
    transform: scale(0.947); transform-origin: top left;
    overflow: hidden;
    background:
      radial-gradient(ellipse 560px 240px at 320px 0px, rgba(80,40,200,0.55), transparent 70%),
      linear-gradient(180deg, #14093a 0%, var(--card-dark) 45%, var(--card-dark) 100%);
    font-family: "Roboto Condensed", sans-serif;
  }
  .photo {
    position: absolute; right: 0; top: 0; width: 640px; height: 627px;
    background:
      radial-gradient(ellipse 190px 230px at 330px 300px, rgba(230,90,120,0.75), transparent 70%),
      radial-gradient(ellipse 420px 300px at 540px 160px, rgba(120,80,255,0.9), transparent 75%),
      linear-gradient(90deg, rgba(40,20,120,0.4) 0%, var(--card-violet) 100%);
    -webkit-mask-image:
      linear-gradient(90deg, transparent 0%, #000 40%),
      linear-gradient(180deg, #000 55%, rgba(0,0,0,0.2) 100%);
    -webkit-mask-composite: source-in;
            mask-image:
      linear-gradient(90deg, transparent 0%, #000 40%),
      linear-gradient(180deg, #000 55%, rgba(0,0,0,0.2) 100%);
            mask-composite: intersect;
  }
  .logo {
    position: absolute; left: 54px; top: 24px;
    font-family: "Roboto Condensed", sans-serif; font-weight: 800;
    font-size: 156px; line-height: 1; letter-spacing: 14px;
    color: var(--logo-pink);
  }
  .heading {
    position: absolute; left: 57px; top: 174px;
    font-weight: 700; font-size: 54px; line-height: 1;
    color: var(--heading-orange);
  }
  .gig { position: absolute; }
  .gig .date {
    display: block; font-family: "Roboto", sans-serif; font-weight: 300;
    font-size: 34px; line-height: 1; color: var(--date-white);
  }
  .gig .venue {
    display: block; margin-top: 6px; font-weight: 700;
    font-size: 30px; line-height: 1; color: var(--venue-yellow);
  }
  .gig .city { font-weight: 400; font-size: 22px; color: var(--city-white); }
  .gig .city.below { display: block; margin-top: 6px; }
  .gig .city.inline { margin-left: 6px; }
  .save {
    position: absolute; left: 742px; top: 505px;
    transform: rotate(-14deg); transform-origin: left top;
    color: var(--save-orange);
  }
  .save .line1 { font-weight: 700; font-size: 38px; line-height: 1; white-space: nowrap; }
  .save .line1 .when { font-family: "Roboto", sans-serif; font-weight: 300; font-size: 50px; }
  .save .festival { font-weight: 700; font-size: 28px; line-height: 1.1; margin-left: 80px; white-space: nowrap; }
  .save .place { font-family: "Roboto", sans-serif; font-weight: 400; font-size: 24px; line-height: 1.1; margin-left: 110px; white-space: nowrap; }
  .save .link { font-weight: 700; font-size: 30px; line-height: 1.2; color: var(--link-blue); margin-left: 80px; white-space: nowrap; }
</style>
</head>
<body>
<main class="stage">
  <section class="card">
    <div class="photo" role="img" aria-label="Photo of the DJ in a hat mixing on turntables under purple and pink club lights"></div>

    <h1 class="logo">QUIVER</h1>
    <h2 class="heading">UPCOMING DATES</h2>

    <div class="gig" style="left:57px; top:240px;">
      <span class="date">3/26/18</span>
      <span class="venue">Velvet Grotto</span>
      <span class="city below">Las Vegas, NV</span>
    </div>
    <div class="gig" style="left:57px; top:365px;">
      <span class="date">4/01/18</span>
      <span class="venue">Lantern Hall</span>
      <span class="city below">Sac, CA</span>
    </div>
    <div class="gig" style="left:57px; top:492px;">
      <span class="date">4/08/18</span>
      <span class="venue">Blue Heron</span>
      <span class="city below">Sac, CA</span>
    </div>

    <div class="gig" style="left:322px; top:242px;">
      <span class="date">5/05/18</span>
      <span class="venue">Open Lanes @ Silver Otter<span class="city inline">Sac, CA</span></span>
    </div>
    <div class="gig" style="left:322px; top:332px;">
      <span class="date">5/10/18</span>
      <span class="venue">Dunmore Fine Gallery<span class="city inline">Sac, CA</span></span>
    </div>
    <div class="gig" style="left:320px; top:426px;">
      <span class="date">5/11/18</span>
      <span class="venue">Bas Rive @ Cafe du Pont<span class="city inline">Sac, CA</span></span>
    </div>
    <div class="gig" style="left:320px; top:523px;">
      <span class="date">5/27/18</span>
      <span class="venue">Sunloft LBW @ Vox<span class="city inline">Sac, CA</span></span>
    </div>

    <div class="save">
      <p class="line1">SAVE THE DATE <span class="when">9/21/18</span></p>
      <p class="festival">MOONWEAVER FESTIVAL</p>
      <p class="place">(PUERTO NUEVO, MX)</p>
      <p class="link">nightlist.net/quiver530</p>
    </div>
  </section>
</main>
</body>
</html>
```